Circulation Rub tube and carton design

We will be launching 3 heat/soothing/circulation rubs, (intense for sports, relaxing for muscles and soothing for aches) and need a portfolio of tube and carton designs to launch with. The product name will be Velmora (Logo Required) and all 3 products will contain Arginine, which is a key feature of the product. We would like to see a bold designs but using earthy tones. Will need an information/ingredients panel on back of tube and carton. Have attached market examples of similar products.
Updates

It will need the following text included 100gm With Arginine for supporting circulation aiding in the temporary relief of Joint and Muscular Pain Joint and Muscular inflammation Stiff Joints Spains, strains, sporting injuries Mild Arthritis

Target Market(s)

there are 3 variants, they will be aimed at 3 different markets. 1. Brelt Intense - for sports 2. Brelt Relax - General population 3. Brelt Soothe - Aged population (arthritis, aches)

Requirements
Must have
• Text to be included 2 separate areas - 100gm & - With Arginine for supporting circulation aiding in the temporary relief of Joint and Muscular Pain Joint and Muscular inflammation Stiff Joints Spains, strains, sporting injuries Mild Arthritis

```html
<!DOCTYPE html>
<html lang="en">
<head>
<meta charset="utf-8">
<title>Velmora Circulation Rub – Tube Range</title>
<link rel="stylesheet" href="https://fonts.googleapis.com/css2?family=Montserrat:ital,wght@0,400;0,800;1,400&display=swap">
<style>
  :root {
    --canvas: #e6e6e6;
    --ink-light: #e9e9e9;
    --silver: #bdbdbd;
    --intense-top: #c2553a;
    --intense-base: #3f5166;
    --soothe-top: #a8782a;
    --soothe-base: #552e16;
    --relax-top: #14454a;
    --relax-base: #4e8a35;
  }
  * { margin: 0; padding: 0; box-sizing: border-box; }
  html, body { width: 1200px; height: 800px; overflow: hidden; }
  body {
    background: var(--canvas);
    font-family: "Montserrat", sans-serif;
    position: relative;
  }
  .range {
    position: absolute;
    inset: 0;
    display: flex;
    justify-content: center;
    align-items: center;
    gap: 100px;
  }
  .tube-face {
    position: relative;
    width: 204px;
    height: 560px;
    overflow: hidden;
    color: var(--ink-light);
  }
  .tube-face .panel-art { position: absolute; inset: 0; width: 100%; height: 100%; }
  .claim {
    position: absolute;
    top: 14px;
    left: 10px;
    right: 10px;
    text-align: center;
    font-style: italic;
    font-weight: 400;
    font-size: 8.6px;
    line-height: 1.02;
  }
  .variant-pill {
    position: absolute;
    left: 24px;
    top: 108px;
    width: 28px;
    height: 196px;
    border-radius: 20px 4px 4px 20px / 28px 4px 4px 28px;
    display: flex;
    justify-content: center;
    padding-top: 40px;
  }
  .variant-name {
    writing-mode: vertical-rl;
    font-size: 17px;
    font-weight: 400;
    white-space: nowrap;
    line-height: 1;
  }
  .variant-name b { font-weight: 400; font-style: italic; }
  .wordmark {
    position: absolute;
    left: 60px;
    top: 108px;
    writing-mode: vertical-rl;
    font-weight: 800;
    font-size: 76px;
    line-height: 1;
    letter-spacing: -1px;
    color: var(--ink-light);
    white-space: nowrap;
  }
  .net-weight {
    position: absolute;
    left: 22px;
    bottom: 26px;
    display: flex;
    flex-direction: column;
    align-items: center;
    gap: 6px;
  }
  .tube-icon { width: 16px; height: 26px; }
  .weight-text {
    writing-mode: vertical-rl;
    font-size: 12px;
    line-height: 1;
  }
  .weight-text strong { font-weight: 800; }
  .weight-text em { font-style: italic; font-weight: 400; }

  .intense .variant-pill { background: var(--intense-base); }
  .soothe .variant-pill { background: var(--soothe-base); }
  .relax .variant-pill { background: var(--relax-base); }
</style>
</head>
<body>
<main class="range">

  <article class="tube-face intense">
    <svg class="panel-art" viewBox="0 0 204 560" preserveAspectRatio="none" aria-hidden="true">
      <rect width="204" height="560" fill="var(--intense-top)"/>
      <polygon points="0,262 102,330 204,262 204,282 102,350 0,282" fill="var(--silver)"/>
      <polygon points="0,282 102,350 204,282 204,560 0,560" fill="var(--intense-base)"/>
      <g stroke="#8f3b28" stroke-width="1.2">
        <line x1="4" y1="2" x2="4" y2="14"/><line x1="10" y1="2" x2="10" y2="14"/><line x1="16" y1="2" x2="16" y2="14"/><line x1="22" y1="2" x2="22" y2="14"/><line x1="28" y1="2" x2="28" y2="14"/><line x1="34" y1="2" x2="34" y2="14"/><line x1="40" y1="2" x2="40" y2="14"/><line x1="46" y1="2" x2="46" y2="14"/><line x1="52" y1="2" x2="52" y2="14"/><line x1="58" y1="2" x2="58" y2="14"/><line x1="64" y1="2" x2="64" y2="14"/><line x1="70" y1="2" x2="70" y2="14"/><line x1="76" y1="2" x2="76" y2="14"/><line x1="82" y1="2" x2="82" y2="14"/><line x1="88" y1="2" x2="88" y2="14"/><line x1="94" y1="2" x2="94" y2="14"/><line x1="100" y1="2" x2="100" y2="14"/><line x1="106" y1="2" x2="106" y2="14"/><line x1="112" y1="2" x2="112" y2="14"/><line x1="118" y1="2" x2="118" y2="14"/><line x1="124" y1="2" x2="124" y2="14"/><line x1="130" y1="2" x2="130" y2="14"/><line x1="136" y1="2" x2="136" y2="14"/><line x1="142" y1="2" x2="142" y2="14"/><line x1="148" y1="2" x2="148" y2="14"/><line x1="154" y1="2" x2="154" y2="14"/><line x1="160" y1="2" x2="160" y2="14"/><line x1="166" y1="2" x2="166" y2="14"/><line x1="172" y1="2" x2="172" y2="14"/><line x1="178" y1="2" x2="178" y2="14"/><line x1="184" y1="2" x2="184" y2="14"/><line x1="190" y1="2" x2="190" y2="14"/><line x1="196" y1="2" x2="196" y2="14"/><line x1="202" y1="2" x2="202" y2="14"/>
      </g>
    </svg>
    <p class="claim">With Arginine for supporting circulation aiding in the temporary relief of Joint and Muscular Pain Joint and Muscular inflammation Stiff Joints Spains, strains, sporting injuries Mild Arthritis</p>
    <div class="variant-pill"><span class="variant-name">Brelt <b>Intense</b></span></div>
    <h2 class="wordmark">Velmora</h2>
    <div class="net-weight">
      <svg class="tube-icon" viewBox="0 0 16 26" aria-hidden="true"><polygon points="2,0 14,0 12,18 10,18 10,22 6,22 6,18 4,18" fill="var(--intense-top)"/></svg>
      <span class="weight-text"><strong>100</strong><em>gm</em></span>
    </div>
  </article>

  <article class="tube-face soothe">
    <svg class="panel-art" viewBox="0 0 204 560" preserveAspectRatio="none" aria-hidden="true">
      <rect width="204" height="560" fill="var(--soothe-top)"/>
      <polygon points="0,262 102,330 204,262 204,282 102,350 0,282" fill="var(--silver)"/>
      <polygon points="0,282 102,350 204,282 204,560 0,560" fill="var(--soothe-base)"/>
      <rect x="0" y="2" width="204" height="12" fill="none" stroke="#80591c" stroke-width="12" stroke-dasharray="1.2 4.8"/>
    </svg>
    <p class="claim">With Arginine for supporting circulation aiding in the temporary relief of Joint and Muscular Pain Joint and Muscular inflammation Stiff Joints Spains, strains, sporting injuries Mild Arthritis</p>
    <div class="variant-pill"><span class="variant-name">Brelt <b>Soothe</b></span></div>
    <h2 class="wordmark">Velmora</h2>
    <div class="net-weight">
      <svg class="tube-icon" viewBox="0 0 16 26" aria-hidden="true"><polygon points="2,0 14,0 12,18 10,18 10,22 6,22 6,18 4,18" fill="var(--soothe-top)"/></svg>
      <span class="weight-text"><strong>100</strong><em>gm</em></span>
    </div>
  </article>

  <article class="tube-face relax">
    <svg class="panel-art" viewBox="0 0 204 560" preserveAspectRatio="none" aria-hidden="true">
      <rect width="204" height="560" fill="var(--relax-top)"/>
      <polygon points="0,262 102,330 204,262 204,282 102,350 0,282" fill="var(--silver)"/>
      <polygon points="0,282 102,350 204,282 204,560 0,560" fill="var(--relax-base)"/>
      <rect x="0" y="2" width="204" height="12" fill="none" stroke="#0c3135" stroke-width="12" stroke-dasharray="1.2 4.8"/>
    </svg>
    <p class="claim">With Arginine for supporting circulation aiding in the temporary relief of Joint and Muscular Pain Joint and Muscular inflammation Stiff Joints Spains, strains, sporting injuries Mild Arthritis</p>
    <div class="variant-pill"><span class="variant-name">Brelt <b>Relax</b></span></div>
    <h2 class="wordmark">Velmora</h2>
    <div class="net-weight">
      <svg class="tube-icon" viewBox="0 0 16 26" aria-hidden="true"><polygon points="2,0 14,0 12,18 10,18 10,22 6,22 6,18 4,18" fill="var(--relax-top)"/></svg>
      <span class="weight-text"><strong>100</strong><em>gm</em></span>
    </div>
  </article>

</main>
</body>
</html>
```